A Vegan Nutritional Supplement (one Product) website

I am looking for an experienced Web designer to build a One Product website for a Nutritional Supplement that is 100% vegan. The emphasis would be on both the Quality and Quantity of the ingredients and their benefits. It contains Essential Vitamins, Minerals, and a proprietary blend of 42 Fruits and Vegetables. I welcome color suggestions as long as it includes Green (vegan) and White.. The final design should communicate to the buyer: Quality, Healthy, Safety (Natural vegan ingredients), Natural energy, well being. The product includes benefits for 3 vital elements of optimal health: Immune Health, Heart Health, and Brain Health

Industry/Entity Type

Health and Wellness - Nutritional Supplements

Number of Pages Required

4 page

Font styles to use
Other font styles liked:
• I Welcome your creativity

Colors
59FF00
82FF00
B8FF75
E3FFCB
F4FFEA

Requirements
Must have
• Options to purchase : One product ($34.95); 2 products ($31.45 each - 10% discount), or 3 Products ($27.95 each - 20% discount)
Nice to have
• Focus on the Benefits of having all these Ingredients - Nutrients in one bottle - Essential Vitamins, Minerals, and proprietary blend of 42 Fruits and Vegetables.

```html
<!DOCTYPE html>
<html lang="en">
<head>
<meta charset="utf-8">
<title>Green Vigor – 100% Vegan Supplement</title>
<link href="https://fonts.googleapis.com/css2?family=Poppins:wght@400;500;600;700;800&display=swap" rel="stylesheet">
<style>
:root{
  --lime:#5cb615;
  --lime-soft:#7ccb33;
  --green:#1f8b34;
  --green-dark:#137a2c;
  --ink:#1c1c1c;
  --muted:#555;
  --card:#f6f6f6;
  --footer:#232323;
  --white:#fff;
}
*{box-sizing:border-box;margin:0;padding:0}
html,body{width:1200px;height:3944px;overflow:hidden}
body{font-family:"Poppins",sans-serif;color:var(--ink);background:var(--white);position:relative}
.abs{position:absolute}
svg{display:block}

/* top bar + nav */
.topbar{left:0;top:0;width:1200px;height:67px;background:var(--lime)}
.contact-chip{display:flex;align-items:center;gap:14px;color:#fff;font-size:18px;top:12px}
.chip-dot{width:43px;height:43px;border-radius:50%;background:#fff;display:flex;align-items:center;justify-content:center}
.top-icon{top:12px;width:43px;height:43px;border-radius:50%;background:#fff;display:flex;align-items:center;justify-content:center}
.navbar{left:0;top:67px;width:1200px;height:111px;background:#fff}
.nav-links{left:436px;top:113px;display:flex;gap:59px;font-size:16px;color:#222}
.brand-box{left:110px;top:0;width:233px;height:178px;background:var(--green-dark);display:flex;align-items:center;justify-content:center}
.brand-name{font-size:28px;font-weight:600;color:#fff;white-space:nowrap}

/* hero */
.hero{left:0;top:178px;width:1200px;height:640px;background:linear-gradient(135deg,#6ec22a,#5fb41b 55%,#7ccb33)}
.hero-title{left:113px;top:380px;color:#fff;font-size:52px;font-weight:700;line-height:85px}
.hero-title span{color:var(--green-dark)}
.btn{display:flex;align-items:center;justify-content:center;border-radius:24px;background:var(--green);color:#fff;font-weight:700;font-size:16px}
.bottle{border-radius:14px;background:linear-gradient(180deg,#f2f2f2 0%,#e4e4e4 20%,#2f6b2a 22%,#3f7d34 70%,#8c5b2f 85%,#e9e9e9 100%)}
.feature{width:222px;height:226px;background:#fff;box-shadow:0 4px 18px rgba(0,0,0,.12);text-align:center;top:735px}
.feature .ico{width:66px;height:66px;border-radius:50%;background:var(--green);margin:25px auto 0;display:flex;align-items:center;justify-content:center}
.feature h3{font-size:23px;font-weight:600;margin-top:22px}
.feature p{font-size:14.5px;color:#333;line-height:23px;margin-top:10px}
.arrow{width:28px;height:28px;border-radius:50%;display:flex;align-items:center;justify-content:center;top:834px}

/* benefits */
.section-title{font-size:31px;font-weight:600;color:var(--green)}
.section-title span{color:var(--lime)}
.ingredient{left:660px;display:flex;align-items:center;gap:32px;font-size:19px;font-weight:600}
.ing-ico{width:56px;height:56px;border-radius:50%;border:2px solid var(--green);display:flex;align-items:center;justify-content:center}

/* welcome */
.welcome{left:0;top:1562px;width:1200px;height:560px;background:linear-gradient(90deg,#5bb523,#3f9e2f 55%,#2e9338)}
.welcome-title{left:112px;top:1672px;color:#fff;font-size:31px;font-weight:600}
.welcome-text{left:112px;top:1737px;width:472px;color:#fff;font-size:15px;line-height:26px;text-align:justify}
.photo-frame{left:629px;top:1658px;width:460px;height:325px;border:7px solid #fff;background:linear-gradient(135deg,#e7a52b,#c83a2a 45%,#8fb53a 75%,#3a3a32)}

/* products */
.product{top:2283px;width:298px;height:387px;background:var(--card)}
.product .media{position:absolute;left:0;top:0;width:100%;height:300px;display:flex;align-items:center;justify-content:center}
.product .info{position:absolute;left:0;bottom:0;width:100%;height:87px;text-align:center;padding-top:20px}
.product h4{font-size:17px;font-weight:600}
.product .price{font-size:14px;font-weight:600;color:var(--green);margin-top:4px}
.product.active .info{background:var(--green);color:#fff}
.product.active .price{color:#fff}
.badge{position:absolute;top:22px;right:22px;width:48px;height:48px;border-radius:50%;background:var(--lime);color:#fff;font-size:15px;font-weight:700;font-style:italic;display:flex;align-items:center;justify-content:center}

/* faq */
.faq-bg{left:0;top:2756px;width:1200px;height:816px;background:linear-gradient(135deg,#e9f3cf,#f6efcf 40%,#e7f1d2 70%,#f1e3c8)}
.faq-item{left:167px;width:868px;height:80px;background:#fff;display:flex;align-items:center;justify-content:space-between;padding:0 44px;font-size:19px;color:#555;box-shadow:0 2px 8px rgba(0,0,0,.05)}
.faq-item b{font-size:26px;color:#444;font-weight:600}

/* footer */
.footer{left:0;top:3572px;width:1200px;height:372px;background:var(--footer);color:#fff}
.foot-brand{left:112px;top:3720px;width:235px;text-align:center}
.foot-h{font-size:18px;font-weight:600;top:3660px}
.foot-list{font-size:15px;line-height:26px;top:3706px}
.foot-row{display:flex;gap:16px;font-size:15px;line-height:26px;align-items:flex-start}
.news-input{left:863px;top:3713px;width:226px;height:38px;background:#fff;border-radius:4px;display:flex;align-items:center;justify-content:space-between;padding-left:14px;font-size:14px;color:#888;overflow:hidden}
.news-btn{width:55px;height:38px;background:var(--lime);display:flex;align-items:center;justify-content:center}
.pay{top:3831px;display:flex;gap:6px;left:863px}
.pay i{display:block;width:31px;height:20px;border-radius:3px;background:#ddd}
.social{top:3894px;width:24px;height:24px;border-radius:50%}
.copyright{left:0;width:1200px;top:3893px;text-align:center;font-size:15px}
</style>
</head>
<body>

<!-- top bar -->
<div class="abs topbar"></div>
<div class="abs contact-chip" style="left:420px">
  <div class="chip-dot"><svg width="18" height="18" viewBox="0 0 24 24"><path fill="#5cb615" d="M6.6 10.8a15 15 0 006.6 6.6l2.2-2.2c.3-.3.7-.4 1-.2 1.1.4 2.3.6 3.6.6.6 0 1 .4 1 1V20c0 .6-.4 1-1 1C10.6 21 3 13.4 3 4c0-.6.4-1 1-1h3.5c.6 0 1 .4 1 1 0 1.3.2 2.5.6 3.6.1.3 0 .7-.2 1z"/></svg></div>
  <span>+1 (555) 014 2200</span>
</div>
<div class="abs contact-chip" style="left:660px">
  <div class="chip-dot"><svg width="18" height="18" viewBox="0 0 24 24"><path fill="#5cb615" d="M6.6 10.8a15 15 0 006.6 6.6l2.2-2.2c.3-.3.7-.4 1-.2 1.1.4 2.3.6 3.6.6.6 0 1 .4 1 1V20c0 .6-.4 1-1 1C10.6 21 3 13.4 3 4c0-.6.4-1 1-1h3.5c.6 0 1 .4 1 1 0 1.3.2 2.5.6 3.6.1.3 0 .7-.2 1z"/></svg></div>
  <span>info@greenvigor.com</span>
</div>
<div class="abs top-icon" style="left:990px"><svg width="18" height="18" viewBox="0 0 24 24"><circle cx="12" cy="8" r="4.5" fill="#5cb615"/><path d="M3.5 21c0-5 3.8-7.5 8.5-7.5s8.5 2.5 8.5 7.5z" fill="#5cb615"/></svg></div>
<div class="abs top-icon" style="left:1044px"><svg width="20" height="20" viewBox="0 0 24 24"><path d="M2 3h3l2.6 11h11L21 6H7" fill="none" stroke="#5cb615" stroke-width="2.4"/><circle cx="9" cy="19" r="2" fill="#5cb615"/><circle cx="17" cy="19" r="2" fill="#5cb615"/></svg></div>

<div class="abs navbar"></div>
<nav class="abs nav-links"><span>HOME</span><span>ABOUT</span><span>PRODUCTS</span><span>BENEFITS</span><span>CONTACT</span></nav>
<svg class="abs" style="left:1060px;top:114px" width="22" height="22" viewBox="0 0 24 24"><circle cx="10" cy="10" r="7" fill="none" stroke="#2aa13a" stroke-width="3"/><path d="M15 15l6 6" stroke="#2aa13a" stroke-width="3.4" stroke-linecap="round"/></svg>

<div class="abs brand-box"><span class="brand-name">Green Vigor</span></div>

<!-- hero -->
<div class="abs hero" role="img" aria-label="Bright green backdrop of fresh vegetables and fruit"></div>
<svg class="abs" style="left:0;top:760px" width="1200" height="70" viewBox="0 0 1200 70" preserveAspectRatio="none"><path fill="#fff" d="M0 22l14-10 10 12 22-6 18 10 26-4 20 14 40-8 30 12 60-2 40 8h760l32-10 20 6 28-14 24 10 30-8 26 4v70H0z"/></svg>
<h1 class="abs hero-title">GREEN VIGOR<br>THAT IS <span>100%</span> VEGAN.</h1>
<div class="abs btn" style="left:113px;top:566px;width:123px;height:46px">SHOP</div>
<div class="abs bottle" style="left:752px;top:268px;width:228px;height:413px" role="img" aria-label="Green Vigor supplement bottle, 90 tablets"></div>

<div class="abs arrow" style="left:205px;background:#fff;box-shadow:0 1px 4px rgba(0,0,0,.2)"><svg width="12" height="12" viewBox="0 0 12 12"><path d="M8 2L4 6l4 4" fill="none" stroke="#333" stroke-width="2"/></svg></div>
<div class="abs arrow" style="left:961px;background:var(--green)"><svg width="12" height="12" viewBox="0 0 12 12"><path d="M4 2l4 4-4 4" fill="none" stroke="#fff" stroke-width="2"/></svg></div>

<div class="abs feature" style="left:251px">
  <div class="ico"><svg width="38" height="38" viewBox="0 0 24 24"><circle cx="12" cy="12" r="8" fill="none" stroke="#fff" stroke-width="1.5"/><circle cx="12" cy="12" r="5" fill="none" stroke="#fff" stroke-width="1.2"/><path d="M9.6 12l1.7 1.7 3.2-3.4" fill="none" stroke="#fff" stroke-width="1.4"/></svg></div>
  <h3>Quality</h3><p>Lorem ipsum dolor sit<br>amet, consectetur</p>
</div>
<div class="abs feature" style="left:490px">
  <div class="ico"><svg width="38" height="38" viewBox="0 0 24 24"><path d="M12 11c-2-3-6-2-5 1 1 2 5 4 5 4s4-2 5-4c1-3-3-4-5-1z" fill="none" stroke="#fff" stroke-width="1.4"/><path d="M4 14c2 4 5 6 8 6s6-2 8-6" fill="none" stroke="#fff" stroke-width="1.4"/></svg></div>
  <h3>Healthy</h3><p>Lorem ipsum dolor sit<br>amet, consectetur</p>
</div>
<div class="abs feature" style="left:727px">
  <div class="ico"><svg width="38" height="38" viewBox="0 0 24 24"><path d="M12 3l7 3v5c0 5-3 8-7 10-4-2-7-5-7-10V6z" fill="none" stroke="#fff" stroke-width="1.5"/><path d="M9 12l2 2 4-4" fill="none" stroke="#fff" stroke-width="1.5"/></svg></div>
  <h3>Safety</h3><p>Lorem ipsum dolor sit<br>amet, consectetur</p>
</div>

<!-- benefits -->
<svg class="abs" style="left:100px;top:1015px" width="480" height="440" viewBox="0 0 480 440"><circle cx="240" cy="220" r="205" fill="none" stroke="#d9d9d9" stroke-width="3" stroke-dasharray="1 9" stroke-linecap="round"/><circle cx="240" cy="220" r="175" fill="none" stroke="#e6e6e6" stroke-width="2" stroke-dasharray="1 10" stroke-linecap="round"/></svg>
<div class="abs bottle" style="left:214px;top:1041px;width:192px;height:360px" role="img" aria-label="Green Vigor supplement bottle"></div>
<h2 class="abs section-title" style="left:660px;top:1043px">Benefits of <span>Ingredients</span></h2>
<div class="abs ingredient" style="top:1116px"><div class="ing-ico"><svg width="28" height="28" viewBox="0 0 24 24"><rect x="3" y="9" width="18" height="7" rx="3.5" transform="rotate(-35 12 12)" fill="none" stroke="#1f8b34" stroke-width="1.5"/></svg></div>Essential Vitamins</div>
<div class="abs ingredient" style="top:1188px"><div class="ing-ico"><svg width="28" height="28" viewBox="0 0 24 24"><path d="M12 3c4 3 5 8 0 14-5-6-4-11 0-14zM12 8v13" fill="none" stroke="#1f8b34" stroke-width="1.5"/></svg></div>Minerals</div>
<div class="abs ingredient" style="top:1260px"><div class="ing-ico"><svg width="28" height="28" viewBox="0 0 24 24"><path d="M3 11h18l-2 8H5z" fill="none" stroke="#1f8b34" stroke-width="1.5"/><circle cx="9" cy="8" r="3" fill="none" stroke="#1f8b34" stroke-width="1.5"/><circle cx="15" cy="8" r="3" fill="none" stroke="#1f8b34" stroke-width="1.5"/></svg></div>42 Fruits</div>
<div class="abs ingredient" style="top:1330px"><div class="ing-ico"><svg width="28" height="28" viewBox="0 0 24 24"><path d="M6 20c-1-6 2-12 7-13 4 0 5 4 4 7-2 4-6 6-11 6z" fill="none" stroke="#1f8b34" stroke-width="1.5"/><path d="M13 7c0-2 1-3 3-4" fill="none" stroke="#1f8b34" stroke-width="1.5"/></svg></div>Vegetables</div>

<!-- welcome -->
<div class="abs welcome" role="img" aria-label="Green toned backdrop of a person enjoying fresh produce in a kitchen"></div>
<svg class="abs" style="left:0;top:2010px" width="1200" height="115" viewBox="0 0 1200 115"><path fill="#fff" d="M0 44l20-6 14 12 30-4 20 10 40-2 30 12 50-6 60 10 80-4 120 8 200-2 160 4 120-6 90 4 60-10 40 2 24-12 22 2 20-16 20-4 30-14 20 4V115H0z"/></svg>
<h2 class="abs welcome-title">Welcome To Green Vigor</h2>
<p class="abs welcome-text">Lorem ipsum dolor sit amet, consectetur adipiscing elit, sed do eiusmod tempor incididunt ut labore et dolore magna aliqua. Ut enim ad minim veniam, quis nostrud exercitation ullamco laboris nisi ut aliquip ex ea commodo consequat. Duis aute irure dolor in reprehenderit in voluptate velit esse cillum dolore eu fugiat nulla pariatur. Excepteur sint occaecat cupidatat non proident, sunt in culpa qui officia deserunt mollit anim id est laborum.</p>
<div class="abs btn" style="left:112px;top:1949px;width:148px;height:46px">LEARN MORE</div>
<div class="abs photo-frame" role="img" aria-label="Bowl of fresh fruit: apples, pears, apricots, grapes and berries"></div>

<!-- products -->
<h2 class="abs section-title" style="left:0;width:1200px;text-align:center;top:2186px">Our <span>Product</span></h2>
<div class="abs product" style="left:112px">
  <div class="media"><div class="bottle" style="width:118px;height:205px" role="img" aria-label="One bottle of Green Vigor"></div></div>
  <div class="info"><h4>One Product</h4><div class="price">$34.95</div></div>
</div>
<div class="abs product active" style="left:449px">
  <div class="media"><div style="position:relative;width:170px;height:200px"><div class="bottle" style="position:absolute;right:0;top:14px;width:90px;height:180px"></div><div class="bottle" style="position:absolute;left:0;top:0;width:105px;height:196px" role="img" aria-label="Two bottles of Green Vigor"></div></div></div>
  <div class="badge">10%</div>
  <div class="info"><h4>Two Products</h4><div class="price">$31.45</div></div>
</div>
<div class="abs product" style="left:787px">
  <div class="media"><div style="position:relative;width:220px;height:200px"><div class="bottle" style="position:absolute;left:0;top:14px;width:85px;height:180px"></div><div class="bottle" style="position:absolute;right:0;top:14px;width:85px;height:180px"></div><div class="bottle" style="position:absolute;left:58px;top:0;width:105px;height:196px" role="img" aria-label="Three bottles of Green Vigor"></div></div></div>
  <div class="badge">20%</div>
  <div class="info"><h4>Three Products</h4><div class="price">$27.95</div></div>
</div>

<!-- faq -->
<div class="abs faq-bg" role="img" aria-label="Soft faded backdrop of assorted fruits"></div>
<h2 class="abs section-title" style="left:0;width:1200px;text-align:center;top:2826px">A Powerful Supplement for <span>Getting Optimal Health</span></h2>
<div class="abs faq-item" style="top:2924px">It May Help Increase Energy (ATP) and Regulate Metabolism<b>+</b></div>
<div class="abs faq-item" style="top:3024px">It May Help the Formation of Red Blood Cells<b>+</b></div>
<div class="abs faq-item" style="top:3126px">It May Help Improve Mental Health<b>+</b></div>
<div class="abs faq-item" style="top:3229px">It May Help Manage Blood Sugar Levels<b>+</b></div>
<div class="abs faq-item" style="top:3335px">It May Help Control Blood Pressure and Improve Blood Flow<b>+</b></div>
<div class="abs btn" style="left:528px;top:3448px;width:146px;height:44px;font-size:15px">LOAD MORE</div>

<!-- footer -->
<footer class="abs footer"></footer>
<div class="abs foot-brand"><span class="brand-name">Green Vigor</span></div>
<div class="abs foot-h" style="left:406px;color:#fff">QUICK LINKS</div>
<div class="abs foot-list" style="left:406px;color:#fff">Home<br>About<br>Services<br>Benefits<br>Contact</div>
<div class="abs foot-h" style="left:589px;color:#fff">CONTACT US</div>
<div class="abs" style="left:589px;top:3710px;color:#fff">
  <div class="foot-row"><svg width="16" height="20" viewBox="0 0 24 24" style="margin-top:4px"><path d="M12 2a7 7 0 00-7 7c0 5 7 13 7 13s7-8 7-13a7 7 0 00-7-7zm0 9.5A2.5 2.5 0 1112 6.5a2.5 2.5 0 010 5z" fill="#fff"/></svg><span>Lorem ipsum dolor<br>sit amet, consectetur</span></div>
  <div class="foot-row" style="margin-top:12px"><svg width="16" height="16" viewBox="0 0 24 24" style="margin-top:5px"><path fill="#fff" d="M6.6 10.8a15 15 0 006.6 6.6l2.2-2.2c.3-.3.7-.4 1-.2 1.1.4 2.3.6 3.6.6.6 0 1 .4 1 1V20c0 .6-.4 1-1 1C10.6 21 3 13.4 3 4c0-.6.4-1 1-1h3.5c.6 0 1 .4 1 1 0 1.3.2 2.5.6 3.6.1.3 0 .7-.2 1z"/></svg><span>+1 (555) 014 2200</span></div>
  <div class="foot-row" style="margin-top:8px"><svg width="16" height="16" viewBox="0 0 24 24" style="margin-top:5px"><rect x="2" y="5" width="20" height="14" rx="2" fill="#fff"/><path d="M2 6l10 7 10-7" fill="none" stroke="#232323" stroke-width="1.8"/></svg><span>info@greenvigor.com</span></div>
</div>
<div class="abs foot-h" style="left:863px;color:#fff">NEWSLETTER</div>
<div class="abs news-input">Ener email<div class="news-btn"><svg width="16" height="14" viewBox="0 0 24 20"><rect x="1" y="2" width="22" height="16" rx="2" fill="#fff"/><path d="M1 3l11 8 11-8" fill="none" stroke="#5cb615" stroke-width="2"/></svg></div></div>
<div class="abs foot-h" style="left:863px;top:3785px;color:#fff">PAYMENT OPTION</div>
<div class="abs pay"><i style="background:#cfcfcf"></i><i style="background:#e6ecf5"></i><i style="background:#dfe6f7"></i><i style="background:#f2f2f2"></i><i style="background:#bcd7f0"></i><i style="background:#f3d8c8"></i></div>
<div class="abs social" style="left:115px;background:#d94a8c"></div>
<div class="abs social" style="left:150px;background:#3b67c2"></div>
<div class="abs social" style="left:186px;background:#e23a2f"></div>
<div class="abs copyright" style="color:#fff">©Copyrights 2022 Green Vigor &nbsp;&nbsp;|&nbsp;&nbsp; All Rights Reserved</div>

</body>
</html>
```